依頼詳細
下記ブランドコンセプトに沿ったご提案をお願い致します。
プロトタイプを添付いたします。構成等、より優れていると思えるご提案がありましたら無視して頂いて構いません。
ブランドコンセプトは以下の通りです。

-- 以下、ブランドコンセプト
「自然が持つ美しさ」と「暮らす人の思い」を取り入れ『生活が楽しい住まい』を創ります
人々に永く愛されてきた天然素材を使用することで自然素材だけが持つ色や質感から確かな手触りと温もりを暮らす人に与え続けてくれます。新しいだけを追い過ぎず自然素材の持つ機能性を生かして自然の働きでしっかりと家を守る
それは流行に左右されない気品を保つ「素朴で美しい風合い」に仕上がります。

住む人のライフスタイルや好みをしっかりとお聞かせいただいた上で土地を生かし隣地環境と調和のある設計を企画し、その人らしい家を一緒に考えていきます。
それはその人がどんなふうに暮らしていきたいのかを一緒に考え、その地で永く暮らしていくイメージを膨らませ生活が楽しくなる様な空間を提案します。
-- 以上、ブランドコンセプト
サイトURL
http://tovaru.com/
ページ数
1ページ
希望イメージ
シンプル 複雑
単色 カラフル
暗い 明るい
日常 高級
遊び心 厳粛
未来的 伝統的
女性的 男性的
希望する色
納品ファイル
補足説明
トップページに関するプロトタイプを「トップページ.png」として添付しております。
また、素材として利用可能なものは下記dropboxリンクよりご利用ください。
https://www.filoshare-box.net/s/7kq2mz/sample-assets

■ 選んだ理由

全員が色使いやコンテンツの配置などを理由として同デザインを選択しました。
似通ったデザインの中でも全員の目を引く、魅力的な部分があったのだと考えます。

■ 提案者全員のお礼・コメント

今回は多くの皆様に貴重なお時間を使って頂きご提案頂きました事、大変うれしく思い感謝申し上げます。
複数名で選考を行いましたが、選考するメンバー全員でどれも素晴らしいデザインだよねと口をそろえて申しておりました。

本当にありがとうございました。

```html
<!DOCTYPE html>
<html lang="ja">
<head>
<meta charset="utf-8">
<title>Tovaru</title>
<link href="https://fonts.googleapis.com/css2?family=Noto+Serif+JP:wght@400;600&family=Noto+Sans+JP:wght@400;500&family=Cormorant+Garamond:wght@500;600&display=swap" rel="stylesheet">
<style>
:root{
  --cream:#f7f3ea;
  --beige:#efe8da;
  --paper:#ffffff;
  --ink:#4a4036;
  --muted:#8b7f70;
  --green:#8cbf3f;
  --green-dark:#6a9a2a;
  --brown:#4d4038;
  --taupe:#7a6e63;
  --line:#d9cfbf;
}
*{box-sizing:border-box;margin:0;padding:0}
html,body{width:1200px;height:4036px;overflow:hidden}
body{background:var(--paper);color:var(--ink);font-family:"Noto Serif JP",serif;position:relative}
.photo{display:block}

/* header */
.site-header{height:180px;background:var(--paper);position:relative;border-bottom:3px solid var(--green)}
.brand{position:absolute;left:0;right:0;top:26px;text-align:center;font-family:"Noto Serif JP",serif;font-weight:400;font-size:38px;line-height:48px;color:var(--taupe);letter-spacing:3px}
.tagline{position:absolute;top:84px;left:0;right:0;text-align:center;font-size:13px;color:var(--muted);letter-spacing:2px}
.header-contact{position:absolute;right:40px;top:14px;width:220px;border:1px solid var(--line);padding:6px 10px;font-family:"Noto Sans JP",sans-serif}
.header-contact small{display:block;font-size:10px;color:var(--muted)}
.header-contact b{font-size:24px;color:var(--green-dark);font-weight:500}
.header-contact .mail{display:inline-block;background:var(--green);color:#fff;font-size:10px;padding:2px 6px;margin-left:6px;vertical-align:4px}
.global-nav{position:absolute;left:86px;right:86px;top:112px;display:flex;height:56px}
.global-nav a{flex:1;text-align:center;border-left:1px solid var(--line);text-decoration:none;color:var(--ink);font-size:14px;padding-top:6px}
.global-nav a:last-child{border-right:1px solid var(--line)}
.global-nav a span{display:block;font-family:"Cormorant Garamond",serif;font-size:12px;color:var(--muted)}
.global-nav a.current{color:var(--green-dark)}

/* hero */
.hero{height:620px;position:relative;display:flex;gap:6px;padding:14px 0}
.hero .side{width:80px;background:linear-gradient(#b8c2cc,#e5e1d8)}
.hero .main{flex:1;background:linear-gradient(135deg,#e9ddc6 0%,#cbb394 55%,#8a6a4b 100%);position:relative}
.hero-copy{position:absolute;left:500px;top:210px;color:#fff;font-size:22px;line-height:2.2;letter-spacing:3px;text-shadow:0 0 8px rgba(0,0,0,.3)}

/* concept */
.concept{height:820px;background:var(--cream);text-align:center;padding-top:80px}
.concept p{font-size:17px;line-height:2.35;letter-spacing:2px}
.leaf{display:block;margin:22px auto}
.btn{display:block;width:1100px;margin:0 auto;height:60px;border:2px solid var(--line);background:var(--paper);text-align:center;line-height:56px;font-size:17px;letter-spacing:3px;color:var(--ink);text-decoration:none;box-shadow:0 3px 0 var(--line)}
.btn::before{content:"";display:inline-block;width:12px;height:12px;background:var(--green);border-radius:50%;margin-right:12px;vertical-align:1px}
.concept .btn{margin-top:56px}

/* section heads */
.section-title{text-align:center;font-size:26px;letter-spacing:8px;font-weight:600}
.section-title svg{display:block;margin:0 auto 6px}

/* works */
.works{height:660px;padding-top:58px}
.works-list{display:flex;gap:36px;justify-content:center;margin:36px 0 40px}
.work{width:316px}
.work .photo{height:250px}
.work p{font-size:13px;margin-top:10px;color:var(--ink)}

/* contact */
.contact{margin:0 86px;height:370px;background:var(--taupe);position:relative;color:#fff}
.contact .photo{position:absolute;left:0;top:0;width:230px;height:170px;background:linear-gradient(#d9d2c4,#9d8f7d)}
.contact-head{position:absolute;left:250px;top:30px}
.contact-head h3{font-size:30px;font-weight:400;letter-spacing:4px}
.contact-head small{font-size:12px;font-family:"Noto Sans JP",sans-serif}
.contact-tel{position:absolute;left:560px;top:28px;font-family:"Noto Sans JP",sans-serif}
.contact-tel small{display:block;font-size:12px}
.contact-tel b{font-size:34px;font-weight:500}
.contact-form{position:absolute;right:30px;top:36px;width:220px;height:50px;border:1px solid #fff;text-align:center;line-height:48px;font-size:15px}
.contact-text{position:absolute;left:60px;right:60px;top:210px;font-size:14px;line-height:2.2;letter-spacing:1px}

/* news */
.news{height:660px;padding-top:64px}
.news-grid{display:grid;grid-template-columns:500px 500px;gap:36px 40px;justify-content:center;margin:36px 0 42px}
.news-item{display:flex;gap:20px;height:170px}
.news-item .photo{width:240px;height:170px;flex:none}
.news-item time{font-family:"Cormorant Garamond",serif;font-size:12px;color:var(--muted);display:block;margin-top:10px}
.news-item h4{font-size:16px;font-weight:600;margin:6px 0 10px}
.news-item p{font-size:12px;line-height:1.8;font-family:"Noto Sans JP",sans-serif;color:var(--muted)}

/* social feed */
.feed{margin:28px 0 0 86px;width:620px;height:300px;border:1px solid var(--line);font-family:"Noto Sans JP",sans-serif}
.feed-head{background:var(--beige);padding:8px 14px;font-size:13px}
.feed-page{display:flex;gap:12px;padding:14px}
.feed-page i{width:50px;height:50px;background:var(--line)}
.feed-page p{font-size:13px}
.feed-fans{display:flex;flex-wrap:wrap;gap:8px;padding:0 14px}
.feed-fans i{width:40px;height:40px;background:var(--beige);border-radius:2px}
.feed-foot{margin:14px;font-size:11px;color:var(--muted)}

.floating{position:absolute;right:36px;top:3590px;width:110px;height:110px;border-radius:50%;background:var(--green);color:#fff;text-align:center;font-size:13px;padding-top:30px;line-height:1.5;font-family:"Noto Sans JP",sans-serif;text-decoration:none}

/* footer */
.site-footer{position:absolute;left:0;right:0;bottom:0;height:316px;background:var(--brown);color:#e8dfd2;text-align:center}
.footer-nav{display:flex;justify-content:center;gap:60px;padding-top:60px;font-size:13px;font-family:"Noto Sans JP",sans-serif}
.site-footer .brand{top:150px;color:#e8dfd2;font-size:34px}
.copyright{position:absolute;bottom:40px;left:0;right:0;font-size:10px;font-family:"Noto Sans JP",sans-serif;letter-spacing:1px}
</style>
</head>
<body>

<header class="site-header">
  <div class="brand">Tovaru</div>
  <p class="tagline">tovaru トヴァル ｜ 山麓市の新築 プロデュース＆注文住宅ブランド</p>
  <div class="header-contact"><small>お問い合わせ・資料請求はこちら</small><b>0120-48-3170</b><span class="mail">メールで</span></div>
  <nav class="global-nav">
    <a class="current" href="#">トップ<span>TOP</span></a>
    <a href="#">家づくり<span>Making House</span></a>
    <a href="#">建築事例<span>Building Case</span></a>
    <a href="#">お問い合わせ<span>Contact Us</span></a>
    <a href="#">資料請求<span>Document Request</span></a>
    <a href="#">会社概要<span>Company Profile</span></a>
  </nav>
</header>

<section class="hero">
  <div class="side photo" role="img" aria-label="住宅外観の写真"></div>
  <div class="main photo" role="img" aria-label="木の床と白壁の明るいリビングの写真">
    <p class="hero-copy">新しいだけを追い過ぎず<br>「素朴で美しい風合い」</p>
  </div>
  <div class="side photo" role="img" aria-label="室内の写真"></div>
</section>

<section class="concept">
  <p>トヴァルブランドでは<br>「自然が持つ美しさ」と「暮らす人の思い」を取り入れ<br>『生活が楽しい住まい』を創ります。</p>
  <svg class="leaf" width="30" height="30" viewBox="0 0 30 30"><path d="M4 26C4 12 14 4 27 3C26 17 18 26 4 26Z" fill="var(--green)"/></svg>
  <p>人々に永く愛されてきた<br>自然素材の機能性を生かして<br>自然の働きでしっかりと家を守る。<br>流行に左右されず、気品を保つ<br>「素朴で美しい風合い」<br>住む人の想いを形に家づくりをお手伝いします。</p>
  <a class="btn" href="#">トヴァルの家づくり</a>
</section>

<section class="works">
  <h2 class="section-title"><svg width="26" height="26" viewBox="0 0 30 30"><path d="M4 26C4 12 14 4 27 3C26 17 18 26 4 26Z" fill="var(--green)"/></svg>建築事例</h2>
  <div class="works-list">
    <div class="work"><div class="photo" role="img" aria-label="キッチンのある室内の施工写真" style="background:linear-gradient(#cfd8dc,#8a7a68)"></div><p>L様Kitchen</p></div>
    <div class="work"><div class="photo" role="img" aria-label="照明と洗面ボウルの施工写真" style="background:linear-gradient(#5a5550,#2e2a27)"></div><p>実例P（1号）</p></div>
    <div class="work"><div class="photo" role="img" aria-label="木製玄関ドアの施工写真" style="background:linear-gradient(90deg,#e3ddd3,#b07c4f,#e3ddd3)"></div><p>実例P（1号）</p></div>
  </div>
  <a class="btn" href="#">施工事例一覧へ</a>
</section>

<section class="contact">
  <div class="photo" role="img" aria-label="窓辺のある室内の写真"></div>
  <div class="contact-head"><h3>お問い合わせ</h3><small>お問い合わせはお気軽にどうぞ</small></div>
  <div class="contact-tel"><small>お電話でのお問い合わせ</small><b>0120-48-3170</b></div>
  <div class="contact-form">コンタクトフォームから</div>
  <p class="contact-text">トヴァルブランドでは住む人のライフスタイルや好みをしっかりとお聞かせいただいた上で土地を生かし隣地環境と調和のある設計を企画し、その人らしい家を一緒に考えていきます。それはその人がどんなふうに暮らしていきたいのかを一緒に考え、その地で永く暮らしていくイメージを膨らませ生活が楽しくなる様な空間を提案します。</p>
</section>

<section class="news">
  <h2 class="section-title"><svg width="26" height="26" viewBox="0 0 30 30"><path d="M4 26C4 12 14 4 27 3C26 17 18 26 4 26Z" fill="var(--green)"/></svg>最新情報</h2>
  <div class="news-grid">
    <article class="news-item"><div class="photo" role="img" aria-label="木のデッキの写真" style="background:linear-gradient(#b08a66,#6e4f36)"></div><div><time>2016/1/25</time><h4>ホームページリニューアルしました</h4><p>新しいサイトを公開しました。施工事例や家づくりの情報を順次お届けします。</p></div></article>
    <article class="news-item"><div class="photo" role="img" aria-label="店舗外観の写真" style="background:linear-gradient(#c7d0d6,#a0927f)"></div><div><time>2016/1/25</time><h4>タイトル</h4><p>本文が入ります。お知らせの内容をここに短くまとめて掲載します。</p></div></article>
    <article class="news-item"><div class="photo" role="img" aria-label="室内の床の写真" style="background:linear-gradient(#3e4c5a,#8c7b68)"></div><div><time>2016/1/25</time><h4>タイトル</h4><p>本文が入ります。お知らせの内容をここに短くまとめて掲載します。</p></div></article>
    <article class="news-item"><div class="photo" role="img" aria-label="レンガ壁の写真" style="background:linear-gradient(#e2d8cb,#b4957a)"></div><div><time>2016/1/25</time><h4>タイトル</h4><p>本文が入ります。お知らせの内容をここに短くまとめて掲載します。</p></div></article>
  </div>
  <a class="btn" href="#">最新情報をもっと見る</a>
</section>

<aside class="feed">
  <div class="feed-head">SNSでチェック</div>
  <div class="feed-page"><i></i><p>トヴァル<br><small>1,984人がトヴァルについて「いいね！」しています。</small></p></div>
  <div class="feed-fans"><i></i><i></i><i></i><i></i><i></i><i></i><i></i><i></i><i></i><i></i><i></i><i></i><i></i><i></i><i></i><i></i><i></i><i></i><i></i><i></i><i></i><i></i></div>
  <p class="feed-foot">SNSページ・プラグイン</p>
</aside>

<a class="floating" href="#">ページの<br>上部へ</a>

<footer class="site-footer">
  <nav class="footer-nav"><span>家づくり</span><span>建築事例</span><span>資料請求</span><span>お問い合わせ</span><span>会社概要</span><span>プライバシーポリシー</span></nav>
  <div class="brand">Tovaru</div>
  <p class="copyright">Copyright © TOVARU HOMES All Rights Reserved.</p>
</footer>

</body>
</html>
```